Lantern Capital Business Card Design Project

We have recently rebranded and would like to design new business cards that incorporate the corporate logo - double sided cards with corporate logo on one side and contact details on the other

Target Market(s)

Sophisticated and high net worth investors and finance industry professionals

Industry/Entity Type

Funds Management

Contact Information for Business Card

The card should prominently feature the company name and logo. Other details will be standard contact details for each staff member - name, address, phone, email, website

Colors
0054AA
0677BA
7BADD7
CADEEF
E8F1F8

Requirements
Must have
• Double-sided design with one side prominently featuring the corporate logo and the other side with all standard contact details

```html
<!DOCTYPE html>
<html lang="en">
<head>
<meta charset="utf-8">
<title>Lantern Capital – Business Card</title>
<link rel="stylesheet" href="https://fonts.googleapis.com/css2?family=Montserrat:wght@700&family=Jost:wght@400&display=swap">
<style>
  :root {
    --backdrop: #d7d7d7;
    --card-white: #ffffff;
    --navy: #1a3d7a;
    --navy-deep: #0b1f40;
    --navy-mid: #173463;
    --ink: #1a3d7a;
    --paper-text: #ffffff;
  }
  * { margin: 0; padding: 0; box-sizing: border-box; }
  html, body {
    width: 1200px; height: 846px; overflow: hidden;
    background: var(--backdrop);
  }
  .sheet {
    position: relative; width: 1200px; height: 846px;
    display: flex; align-items: center; justify-content: center; gap: 60px;
  }
  .card {
    position: relative; width: 520px; height: 317px;
    box-shadow: 0 8px 24px rgba(0,0,0,0.18);
    overflow: hidden;
  }

  /* Front: contact details */
  .card--front { background: var(--card-white); }
  .holder-name {
    position: absolute; left: 34px; top: 118px;
    font-family: "Montserrat", sans-serif; font-weight: 700;
    font-size: 17px; color: var(--ink);
  }
  .contact-list {
    position: absolute; right: 30px; top: 26px;
    list-style: none; text-align: right;
    font-family: "Jost", sans-serif; font-size: 12.5px; color: var(--ink);
    line-height: 19px;
  }
  .contact-list li { display: flex; justify-content: flex-end; align-items: center; gap: 8px; }
  .contact-list svg { width: 13px; height: 13px; fill: var(--ink); flex: none; }
  .wordmark-front {
    position: absolute; left: 70px; top: 172px;
    display: flex; align-items: center; gap: 14px;
  }
  .wordmark-dot { width: 28px; height: 28px; border-radius: 50%; background: var(--navy); }
  .wordmark-text {
    font-family: "Jost", sans-serif; font-weight: 400;
    font-size: 36px; line-height: 1; color: var(--navy);
  }
  .address-band {
    position: absolute; left: 0; right: 0; top: 236px; height: 34px;
    background: var(--navy);
    display: flex; align-items: center; justify-content: flex-end; padding-right: 30px;
    font-family: "Jost", sans-serif; font-size: 12.5px; color: var(--paper-text);
  }

  /* Back: logo side */
  .card--back { background: var(--navy-deep); }
  .back-photo {
    position: absolute; inset: 0;
    background: linear-gradient(135deg, var(--navy-deep) 0%, var(--navy-mid) 55%, var(--navy-deep) 100%);
  }
  .wordmark-back {
    position: absolute; inset: 0;
    display: flex; align-items: center; justify-content: center;
    font-family: "Jost", sans-serif; font-weight: 400;
    font-size: 42px; color: var(--paper-text);
  }
</style>
</head>
<body>
<main class="sheet">
  <section class="card card--front" aria-label="Business card front">
    <p class="holder-name">Sam Hartley</p>
    <ul class="contact-list">
      <li>+02 9400 1157
        <svg viewBox="0 0 16 16" aria-hidden="true"><path d="M4 1l2.5 3-1.5 1.6c.8 2 2.4 3.6 4.4 4.4L11 8.5l3 2.5-1.2 2.6C8 13.4 2.6 8 2.4 3.2z"/></svg>
      </li>
      <li>sam.hartley@lantern-cap.com
        <svg viewBox="0 0 16 16" aria-hidden="true"><path d="M1 3h14v10H1z M2 4.2v.4l6 4.3 6-4.3v-.4z" fill-rule="evenodd"/></svg>
      </li>
      <li>www.lantern-cap.com
        <svg viewBox="0 0 16 16" aria-hidden="true"><circle cx="8" cy="8" r="7"/><path d="M1 8h14M8 1c-3 3.5-3 10.5 0 14M8 1c3 3.5 3 10.5 0 14M2.5 4.5h11M2.5 11.5h11" stroke="#fff" stroke-width="1" fill="none"/></svg>
      </li>
    </ul>
    <div class="wordmark-front">
      <span class="wordmark-dot" aria-hidden="true"></span>
      <span class="wordmark-text">Lantern Capital</span>
    </div>
    <div class="address-band">Level 14 Harbour Tower, 21 Kent Street, Sydney NSW 2000</div>
  </section>

  <section class="card card--back" aria-label="Business card back">
    <div class="back-photo" role="img" aria-label="Dark blue toned photograph of classical stone columns"></div>
    <p class="wordmark-back">Lantern Capital</p>
  </section>
</main>
</body>
</html>
```